Web site for Physical Therapy Clinic

Looking for a web designer who has experience in planning & designing graphic user interfaces for web site.
You will be delivered a sitemap/flow diagram and a general visual concept and expected to deliver finished web GUI design in PSD (or any suitable) format.
RESPONSIBILITIES:
-Interpreting the sitemap/flow diagram into an user interface
-Developing a visual concept which aligns with the brands and project goals
-Building wireframes
-Design usable, technically feasible, great looking user interfaces in Photoshop(or Illustrator)
-Present your design in jpg format
-Delivering pixel perfect design ready to be converted to html/css
EXPECTATIONS:
-Adobe Creative Suite
-Deliver quality design by applying sound design practices with solid methodology, workflow & discipline.
-Manage the design process from start to finish, including gathering requirements and delivering final assets
-Strong sense of design and knowledge of typography, grid systems, color theory, usability, interactivity and information architecture principles
-Familiar with HTML, CSS, and JavaScript knowledge for optimizing design concepts around these technologies
-Familiar with standards-based, cross-browser, multi-device design
-Familiar with responsive web design/development
-Participate in estimating project efforts and delivery timelines
-Identify technical, schedule, and other project risks and provide relevant feedback
-Proactively collaborate and communicate
-Ability to multitask and prioritize multiple concurrent assignments
-High attention to detail
Corvela Physical Therapy provides personalized and high-quality therapy services. Patients are treated in two different settings; at our outpatient clinic or through home health visits. The services we provide are: Physical Therapy, Occupational Therapy, Speech Therapy and Massage Therapy.
We are looking for a designer/developer to build a fully-functional website for our business. The website needs to be:
• Fast-loading
• Mobile-compatible
• User-friendly
The following web address has been secured through namebarrow.example:
www.corvelapt.example
Tabs for the website will include...
Home
About
• History
• Team
Patients
• Services
• Insurances & payments accepted
• Coverage areas
Agencies
• Inquiries
• Forms & credentials
• Coverage areas
Therapists
• Reasons to work with us
• Career opportunities
• Application
FAQ
Contact
• Inquiries
• Locations
Breakdown of content needed on each page:
HOME
• Tagline
ABOUT
• History
• Team
PATIENTS
• Pain Management
- Neck & back pain
- Radiculopathy
- Sacroiliac Joint Syndrome
- Status Post Laminectomy
- Status Post Spinal Fusion
- Patellafemoral pain
- Arthritis: Osteoarthritis & Rheumatoid Arthritis
- Temporomandibular Joint
- Post-amputation
• Neurological Disorders
- Cerebral Vascular Accidents
- Parkinson's disease
- Multiple Sclerosis
- Traumatic & non-traumatic Brain Injury
- Spinal cord injury
- Guillain Barre
- Intracranial hemorrhage
- Diabetic neuropathy
- Post Polio Syndrome
• Work/Sport Injuries
- Carpal Tunnel Syndrome
- Disc Hernia
- Plantar Fasciitis
- Sciatica
- Frozen Shoulder
- Rotator Cuff injury/surgery
- Hip surgery
- Knee surgery: Anterior/Posterior Cruciate Ligament & Meniscal Tear
- Ankle sprain
- Tennis Elbow
- Golfer's Elbow
• Services
- Outpatient
- Home Health (with coverage area maps)
• Languages
- English
- Spanish
- Vietnamese
- Farsi
- Mandarin
- Tagalog
• Insurances Accepted
- HMO
- PPO
- Medicare
- Workers Compensation
• Physician Referral Form (printable PDF)
• Patient Registration Form (able to sign and print)
AGENCIES
• Physical Therapy Coverage Areas with map
• Occupational Therapy Coverage Areas with map
• Speech Therapy Coverage Areas with map
• Inquiry Form that goes directly to Corvela email
- Name
- Title
- Company
- Phone Number
- Email
- Question
• Password access to Credentials & Contact List (editable)
THERAPISTS
• Reasons to work with us
- check example (http://www.ostrandrehab.example/#!therapists/c10my)
- add Referral Bonus
• Career Opportunities editable through an excel worksheet
• Application form that goes directly to Corvela email
- check example (http://www.ostrandrehab.example/#!therapist-application-/cp7d)
FAQ
CONTACT
• Inquiry form
- option of "Agency" or "Patient"
- option of "Home Health Services" or "Outpatient Clinic"
- Question
• Clinic Location & Hours
30587 Marlowe Ave., Suite 12
Larkmoor, CA 90417
Monday - Friday 9am - 6pm
• Home Health Office Hours
Monday - Friday 9:30am - 6:30pm
• Connect to social networks
- Linkedin
https://www.linkedin.com/profile/view?id=517093648&authType=NAME_SEARCH&authToken=qmRt&locale=en_US&trk=tyah&trkInfo=tarId%3A1598304716025%2Ctas%3Acorvela%20physical%20%2Cidx%3A1-1-1
- Facebook
https://www.facebook.com/pages/Corvela-Physical-Therapy/580917264315
Target Market(s)
Adult patients ages 18 to 80 in need of pain management and/or rehab. Home health agencies that contract therapists.
Industry/Entity Type
Architecture
Look and feel

```html
<!DOCTYPE html>
<html lang="en">
<head>
<meta charset="utf-8">
<title>Corvela Physical Therapy</title>
<link rel="stylesheet" href="https://fonts.googleapis.com/css2?family=PT+Sans:wght@400;700&family=Open+Sans:wght@400;600&display=swap">
<style>
:root{
  --blue:#237cb9;
  --red:#a8161c;
  --logo:#8a1c22;
  --ink:#1e1e1e;
  --text:#6f6f6f;
  --rule:#e2e2e2;
  --bar:#efefef;
  --footer:#232323;
  --footer-deep:#1b1b1b;
  --footer-text:#9a9a9a;
  --link:#3aa0e0;
}
*{margin:0;padding:0;box-sizing:border-box}
html,body{width:1200px;height:2281px;overflow:hidden;background:#fff}
body{position:relative;font-family:"PT Sans",sans-serif;color:var(--ink)}
.abs{position:absolute}

/* header */
.site-header{position:absolute;left:0;top:0;width:1200px;height:106px;background:#fff}
.brand{position:absolute;left:61px;top:34px;display:flex;align-items:center;gap:10px}
.brand-mark{width:14px;height:14px;background:var(--logo)}
.brand-name{font-family:"PT Sans",sans-serif;font-weight:700;font-size:22px;color:var(--logo);letter-spacing:.5px}
.main-nav a{position:absolute;top:33px;height:40px;line-height:40px;font-family:"Open Sans",sans-serif;font-size:14px;color:#222;text-decoration:none;white-space:nowrap}
.main-nav a.active{background:var(--blue);color:#fff;padding:0 13px;left:532px}

/* hero */
.hero{position:absolute;left:0;top:106px;width:1200px;height:537px;
  background:linear-gradient(100deg,#3c3a36 0%,#5a5650 35%,#6b5a4e 60%,#8a6a5a 80%,#5c4a40 100%)}
.hero-shade{position:absolute;inset:0;background:rgba(0,0,0,.25)}
.hero-title{position:absolute;left:0;right:0;top:218px;text-align:center;color:#fff;font-size:70px;font-weight:400;letter-spacing:2px;font-family:"PT Sans",sans-serif;line-height:1}
.hero-dots{position:absolute;top:502px;left:576px;display:flex;gap:10px}
.hero-dots span{width:8px;height:8px;border-radius:50%;background:rgba(255,255,255,.4)}
.hero-dots span.on{background:#fff}

/* section headings */
.section-title{position:absolute;font-size:24px;font-weight:400;letter-spacing:.5px;color:var(--ink);line-height:1.3}

/* services */
.service{position:absolute;width:339px}
.service-photo{width:339px;height:187px}
.service h3{font-size:22px;font-weight:400;margin:34px 0 0 11px;line-height:1}
.service p{font-family:"Open Sans",sans-serif;font-size:12px;line-height:20.5px;color:var(--text);margin:12px 44px 0 11px;text-align:justify}
.service .more{display:block;font-family:"Open Sans",sans-serif;font-size:10px;color:var(--red);margin:10px 0 0 11px;text-decoration:none}
.service .rule{position:absolute;left:0;right:0;height:1px;background:var(--rule)}

/* news */
.news{position:absolute;left:797px;width:327px}
.news-meta{display:flex;gap:8px;height:33px}
.news-date{width:88px;height:33px;background:var(--blue);color:#fff;font-family:"Open Sans",sans-serif;font-size:12px;line-height:33px;text-align:center;border-bottom-left-radius:3px;border-bottom-right-radius:18px 8px}
.news-count{width:27px;height:30px;background:#1c1c1c;color:#fff;font-family:"Open Sans",sans-serif;font-size:12px;line-height:30px;text-align:center}
.news h4{font-size:17px;font-weight:400;color:var(--blue);line-height:27px;margin-top:30px;max-width:290px}
.news p{font-family:"Open Sans",sans-serif;font-size:12px;line-height:22px;color:var(--text);margin-top:10px;text-align:justify}
.arrow{color:#555;margin-left:6px}

/* settings */
.setting{position:absolute;left:800px;display:flex;align-items:center;gap:20px;font-family:"Open Sans",sans-serif;font-size:19px;color:#666}
.setting svg{width:28px;height:28px}

/* therapists */
.portrait{position:absolute;width:116px;height:116px;border-radius:50%}
.name-bar{position:absolute;height:46px;background:var(--bar)}
.name-bar .icon{position:absolute;left:0;top:0;width:48px;height:46px;background:var(--blue);display:flex;align-items:center;justify-content:center}
.name-bar .name{position:absolute;left:64px;top:10px;font-size:21px;color:#222}
.name-bar .name em{font-family:"PT Sans",serif;font-style:italic;font-size:13px;font-weight:700}
.bio{position:absolute;font-family:"Open Sans",sans-serif;font-size:13px;line-height:22px;color:var(--text)}
.t-rule{position:absolute;height:1px;background:var(--rule)}
.email{position:absolute;font-family:"Open Sans",sans-serif;font-size:16px;color:#222}
.email b{font-weight:400;color:var(--blue)}
.socials{position:absolute;display:flex;gap:14px}
.socials span{width:11px;height:11px;border-radius:50%;background:#c9c9c9}

/* footer */
.site-footer{position:absolute;left:0;top:1850px;width:1200px;height:431px;background:var(--footer)}
.footer-bottom{position:absolute;left:0;top:372px;width:1200px;height:59px;background:var(--footer-deep);border-top:1px solid #2e2e2e}
.f-title{position:absolute;top:26px;color:#fff;font-size:22px;font-weight:400}
.f-text{position:absolute;font-family:"Open Sans",sans-serif;font-size:11px;line-height:20px;color:var(--footer-text)}
.f-sub{position:absolute;color:#fff;font-size:18px;font-weight:400}
.f-nav{position:absolute;top:30px;display:flex;gap:6px}
.f-nav span{width:31px;height:29px;border:1px solid #555;color:#fff;font-size:16px;line-height:27px;text-align:center}
.f-item{position:absolute;font-family:"Open Sans",sans-serif;font-size:11px;line-height:20px;color:var(--footer-text);padding-left:22px}
.f-item::before{content:"\2192";position:absolute;left:0;top:0;color:#ddd}
.f-item time{display:block;color:var(--link);margin-top:3px}
.copyright{position:absolute;left:61px;top:22px;font-family:"Open Sans",sans-serif;font-size:9px;color:#8a8a8a}
.to-top{position:absolute;left:1126px;top:14px;color:#fff;font-size:16px}
</style>
</head>
<body>

<header class="site-header">
  <div class="brand">
    <span class="brand-mark"></span>
    <span class="brand-name">Corvela Physical Therapy</span>
  </div>
  <nav class="main-nav">
    <a class="active" href="#">Home</a>
    <a href="#" style="left:617px">About Us</a>
    <a href="#" style="left:712px">Patients</a>
    <a href="#" style="left:800px">Physicians</a>
    <a href="#" style="left:903px">Therapists</a>
    <a href="#" style="left:1007px">FAQ</a>
    <a href="#" style="left:1066px">Contact</a>
  </nav>
</header>

<section class="hero" role="img" aria-label="Smiling therapist holding a tablet in a clinic gym with patients exercising behind her">
  <div class="hero-shade"></div>
  <h1 class="hero-title">LOREM IPSUM DOLOR AMET</h1>
  <div class="hero-dots"><span class="on"></span><span></span><span></span></div>
</section>

<h2 class="section-title" style="left:61px;top:672px">WHAT WE DO</h2>

<article class="service" style="left:61px;top:727px">
  <div class="service-photo" role="img" aria-label="Therapist stretching a patient's leg on a treatment table in a gym" style="background:linear-gradient(135deg,#c9c2b4,#8d8a82 50%,#b59a86)"></div>
  <h3>Physical Therapy</h3>
  <p>Maecenas etos sit amet, consectetur adipiscing elit. Terminal volutpat rutrum metro amet sollicitudin interdum. Suspendisse pulvinar, velit etos pharetra interdum, ante tellus gravida mollis tellus neque vitae elit.</p>
  <a class="more" href="#">READ MORE</a>
  <div class="rule" style="top:389px"></div>
</article>

<article class="service" style="left:429px;top:727px">
  <div class="service-photo" role="img" aria-label="Speech therapist working with an elderly woman at a table outdoors" style="background:linear-gradient(135deg,#5f7a3e,#a39a8e 50%,#d0bcc0)"></div>
  <h3>Speech Therapy</h3>
  <p>Maecenas etos sit amet, consectetur adipiscing elit. Terminal volutpat rutrum metro amet sollicitudin interdum. Suspendisse pulvinar, velit etos pharetra interdum, ante tellus gravida mollis tellus neque vitae elit.</p>
  <a class="more" href="#">READ MORE</a>
  <div class="rule" style="top:389px"></div>
</article>

<article class="service" style="left:61px;top:1144px">
  <div class="service-photo" role="img" aria-label="Occupational therapists helping a child in a wheelchair in a classroom" style="background:linear-gradient(135deg,#a88a6e,#7c8aa0 50%,#2f4e78)"></div>
  <h3>Occupational Therapy</h3>
  <p>Lorem ipsum dolor sit amet, consectetur adipiscing elit. Ut volutpat rutrum eros sit amet sollicitudin. Suspendisse pulvinar, velit nec pharetra interdum, ante tellus ornare mi, et mollis tellus neque vitae elit.</p>
  <a class="more" href="#">READ MORE</a>
  <div class="rule" style="top:397px"></div>
</article>

<article class="service" style="left:429px;top:1144px">
  <div class="service-photo" role="img" aria-label="Woman receiving a back massage" style="background:linear-gradient(135deg,#e6e8ea,#c8b2a2 55%,#9a7a68)"></div>
  <h3>Massage Therapy</h3>
  <p>Lorem ipsum dolor sit amet, consectetur adipiscing elit. Ut volutpat rutrum eros sit amet sollicitudin. Suspendisse pulvinar, velit nec pharetra interdum, ante tellus ornare mi, et mollis tellus neque vitae elit.</p>
  <a class="more" href="#">READ MORE</a>
  <div class="rule" style="top:397px"></div>
</article>

<h2 class="section-title" style="left:797px;top:672px">LATEST NEWS</h2>

<article class="news" style="top:727px">
  <div class="news-meta"><span class="news-date">14 NOV 14</span><span class="news-count">5</span></div>
  <h4>Massa ad minim veniamquis nostrud exercitation estullamco.</h4>
  <p>Nam libero tempore, cum soluta nobis est eligendi opticumque nihil impedit quo minus id quod maxime placeat facerepossimus, repellendus... <span class="arrow">&#10230;</span></p>
</article>
<article class="news" style="top:939px">
  <div class="news-meta"><span class="news-date">03 DEC 14</span><span class="news-count">7</span></div>
  <h4>Ut enim ad minim veniamquis nostrud ullamco reprehenderit in volup.</h4>
  <p>Nam libero tempore, cum soluta nobis est eligendi opticumque nihil impedit quo minus id quod maxime placeat facerepossimus, repellendus... <span class="arrow">&#10230;</span></p>
</article>
<article class="news" style="top:1151px">
  <div class="news-meta"><span class="news-date">23 DEC 14</span><span class="news-count">34</span></div>
  <h4>Massa ad minim veniamquis nostrud exercitation estullamco.</h4>
  <p>Nam libero tempore, cum soluta nobis est eligendi opticumque nihil impedit quo minus id quod maxime placeat facerepossimus, repellendus... <span class="arrow">&#10230;</span></p>
</article>

<h2 class="section-title" style="left:797px;top:1354px;width:340px">WE TREAT OUR IN TWO DIFFERENT SETTINGS</h2>
<div class="setting" style="top:1437px">
  <svg viewBox="0 0 28 28" fill="none" stroke="#237cb9" stroke-width="2.4" stroke-linecap="round"><path d="M5 3v8a6 6 0 0 0 12 0V3"/><path d="M11 17v3a5 5 0 0 0 10 0v-4"/><circle cx="21" cy="13" r="3"/></svg>
  <span>At our outpatient clinic</span>
</div>
<div class="setting" style="top:1485px">
  <svg viewBox="0 0 28 28" fill="#237cb9"><path d="M14 3 2 14h4v11h6v-7h4v7h6V14h4z"/></svg>
  <span>Home health visits</span>
</div>
<div class="abs" style="left:797px;top:1542px;width:341px;height:1px;background:var(--rule)"></div>

<h2 class="section-title" style="left:61px;top:1577px">OUR THERAPISTS</h2>

<div class="portrait" role="img" aria-label="Portrait of therapist Thomas" style="left:62px;top:1634px;background:radial-gradient(circle at 50% 40%,#c9a88e,#8b97a6 70%,#e4e6ea)"></div>
<div class="name-bar" style="left:208px;top:1632px;width:375px">
  <span class="icon"><svg width="22" height="22" viewBox="0 0 22 22" fill="#fff"><circle cx="11" cy="7" r="5"/><path d="M2 21a9 8 0 0 1 18 0z"/></svg></span>
  <span class="name">Thomas, <em>Dolor sit amet</em></span>
</div>
<p class="bio" style="left:208px;top:1693px;width:375px">Lorem ipsum dolor sit amet, consectetuer adipiscing elit, sed diam nonummy nibh euismod tincidunt ut laoreet dolore magna aliquam erat volutpat.</p>
<div class="t-rule" style="left:208px;top:1780px;width:375px"></div>
<p class="email" style="left:208px;top:1788px"><b>Email :</b> yourname@mailbox.example</p>
<div class="socials" style="left:510px;top:1795px"><span></span><span></span><span></span></div>

<div class="portrait" role="img" aria-label="Portrait of therapist Lara" style="left:619px;top:1634px;background:radial-gradient(circle at 50% 40%,#a8785e,#3e5f86 70%,#e4e6ea)"></div>
<div class="name-bar" style="left:765px;top:1632px;width:373px">
  <span class="icon"><svg width="22" height="22" viewBox="0 0 22 22" fill="#fff"><circle cx="11" cy="7" r="5"/><path d="M2 21a9 8 0 0 1 18 0z"/></svg></span>
  <span class="name">Lara, <em>Dolor sit amet</em></span>
</div>
<p class="bio" style="left:765px;top:1693px;width:373px">Lorem ipsum dolor sit amet, consectetuer adipiscing elit, sed diam nonummy nibh euismod tincidunt ut laoreet dolore magna aliquam erat volutpat.</p>
<div class="t-rule" style="left:765px;top:1780px;width:373px"></div>
<p class="email" style="left:765px;top:1788px"><b>Email :</b> yourname@mailbox.example</p>
<div class="socials" style="left:1065px;top:1795px"><span></span><span></span><span></span></div>

<footer class="site-footer">
  <h3 class="f-title" style="left:61px">Corvela Physical Therapy</h3>
  <p class="f-text" style="left:61px;top:70px;width:330px">Lorem ipsum dolor sit amet, consectetuer adipiscing elit, sed diam nonummy nibh euismod tincidunt.</p>
  <h4 class="f-sub" style="left:61px;top:126px">Address</h4>
  <p class="f-text" style="left:61px;top:156px;line-height:16px">30587 Marlowe Ave., Suite 12<br>Larkmoor, CA 90417<br>Monday - Friday 9am - 6pm</p>
  <p class="f-text" style="left:239px;top:156px;line-height:16px">4816 Tasman Way, Suite 7<br>Larkmoor, CA 90419<br>Monday - Friday 9:30am - 6:30pm</p>

  <h3 class="f-title" style="left:497px">Latest Posts</h3>
  <div class="f-nav" style="left:704px"><span>&larr;</span><span>&rarr;</span></div>
  <p class="f-item" style="left:497px;top:72px">Euismod tincidunt ut laoreet dolore magna<time>about a year ago</time></p>
  <p class="f-item" style="left:497px;top:132px">Sed diam nonummy nibh euismod tincidunt<time>one day ago</time></p>
  <p class="f-item" style="left:497px;top:192px">Lorem ipsum dolor sit amet consectetuer<time>2 years ago</time></p>

  <h3 class="f-title" style="left:867px">Latest Tweets</h3>
  <div class="f-nav" style="left:1071px"><span>&larr;</span><span>&rarr;</span></div>
  <p class="f-item" style="left:867px;top:72px;width:250px">Lorem ipsum dolor sit amet, consectetuer adipiscing elit, sed diam nonummy nibh euismod tincidunt ut laoreet<time>8 days ago</time></p>
  <p class="f-item" style="left:867px;top:177px;width:250px">Lorem ipsum dolor sit amet, consectetuer adipiscing elit, sed diam nonummy nibh euismod tincidunt ut laoreet<time>one month ago</time></p>
  <p class="f-item" style="left:867px;top:282px;width:250px">Lorem ipsum dolor sit amet, consectetuer adipiscing elit, sed diam nonummy.<time>19 days ago</time></p>

  <div class="footer-bottom">
    <p class="copyright">Copyright &copy; 2015 Corvela Physical Therapy.All Rights Reserved.</p>
    <span class="to-top">&uarr;</span>
  </div>
</footer>

</body>
</html>
```